Web Design for Webdesign company 3 page PSD

Project
---------
We need a PSD Web Design to be used in a WordPress installation.
What we would like to create is a professional looking website for a web design agency. We also need you to look for suitable stock images to be placed on these pages.
We need the design for:
Homepage
Landing page
Contact page
attached in the pages file you will find a file with more in depth details how these files should be build up.
We would like to see a desktop version and a mobile version of these pages
The website should have a 1100px width.
The mobile design should have 480px width.
The homepage should have a header slider about 450px high.
The slider is preferred full width and should have some images text and a button
Objectives
-------------
The main objective for the website is to get leads from customers in the form of a request for a quotation or a call or mail me back action. The most important action for the homepage is to link and navigate to our landing pages.
What we want to tell our visitors (our main products)
-------------------------------------------------------------------
- A website with no big investment but a monthly rate
- A successful website with no worries (a complete website, seo, hosting and a service contract for future customization is included for a monthly rate)
Color Scheme
------------
Use branding colors. You can find them in the branding.pdf file.
Additional colors:
White: #ffffff
Black: #181818
Company info
--------------
We are a starting web design / marketing agency based in The Netherlands and looking for the design of our website. Our services are (custom) webdesign, website marketing or combinations of both. Our main customer group is small business owners.
We sell websites but give the option to buy it with a lease contract.
A second product is a default website with a complete service: SEO, hosting and a service contract for a monthly rate.
Content:
-----------
If not available place Lorem Ipsum text.
There will come about 400 words of text on the landing pages
Design Competition
--------------------------
Since this is a designing competition we would like to see your creativity.
What you can expect from us is a lot of feedback 7 days a week with short response time.
You can send us the first sketchy mock ups of the homepage and we will give feedback based on these design. But we like your feedback or comments as well
Read the pages file for more in depth details how the pages should be designed

Target Market(s)
Small business owners in The Netherlands
Industry/Entity Type
It Company
Number of Pages Required
3 page
Requirements
Must have
- Homepage:
- Header slider with images, some text and a link to a custom page
- The slider should have 3 designed slides
- Landings page:
- Sidebar
- Action button for a request for a quotation
- Action button for a call me back action
- Action button for an appointment
- Contact form:
- Address details
- Contact form
Nice to have
- Homepage:
- Full width slider
- Testimonial block
- Blog items
Should not have
- Flash
- A to crowded design

```html
<!DOCTYPE html>
<html lang="en">
<head>
<meta charset="utf-8">
<title>Quillmoor – Responsive Web Design</title>
<link rel="stylesheet" href="https://fonts.googleapis.com/css2?family=Open+Sans:ital,wght@0,300;0,400;0,600;0,700;1,400;1,600&display=swap">
<style>
  :root {
    --teal: #3e7f83;
    --teal-panel: rgba(62, 127, 131, 0.93);
    --menu-bg: rgba(62, 110, 114, 0.55);
    --menu-line: rgba(20, 40, 42, 0.55);
    --white: #ffffff;
    --black: #181818;
    --photo-dark: #2b2a2a;
    --photo-mid: #4a4745;
    --photo-light: #6a6663;
    --dot: rgba(255, 255, 255, 0.55);
  }
  * { box-sizing: border-box; margin: 0; padding: 0; }
  html, body {
    width: 1200px; height: 660px; overflow: hidden;
    background: var(--black);
    font-family: "Open Sans", Arial, sans-serif;
    color: var(--white);
  }
  .hero { position: relative; width: 1200px; height: 660px; overflow: hidden; }
  .hero__photo {
    position: absolute; inset: 0;
    background:
      radial-gradient(ellipse 420px 520px at 820px 330px, var(--photo-light) 0%, rgba(90,86,83,0.6) 40%, transparent 75%),
      linear-gradient(160deg, var(--photo-mid) 0%, var(--photo-dark) 55%, #232222 100%);
  }
  .hero__shade { position: absolute; inset: 0; background: rgba(24, 24, 24, 0.22); }

  .brand {
    position: absolute; left: 0; top: 0; width: 221px; height: 167px;
    background: var(--teal-panel);
    display: flex; flex-direction: column; align-items: center; justify-content: center;
    gap: 14px; text-align: center;
  }
  .brand__mark { width: 44px; height: 44px; border-radius: 50%; background: rgba(255,255,255,0.2); }
  .brand__name { font-weight: 700; font-size: 19px; line-height: 1; letter-spacing: 0.5px; }

  .actions { position: absolute; left: 0; top: 167px; width: 221px; list-style: none; }
  .actions__item {
    height: 61px; display: flex; align-items: center; gap: 14px; padding-left: 19px;
    background: var(--menu-bg); border-top: 1px solid var(--menu-line);
  }
  .actions__icon { width: 25px; height: 25px; flex: none; }
  .actions__title { font-size: 12.5px; font-weight: 700; text-transform: uppercase; line-height: 1.3; }
  .actions__link { font-size: 11px; font-style: italic; font-weight: 600; line-height: 1.4; }

  .slide { position: absolute; left: 0; right: 0; top: 268px; text-align: center; }
  .slide__title { font-size: 40px; font-weight: 700; letter-spacing: 0.5px; line-height: 1.2; text-transform: uppercase; }
  .slide__subtitle { font-size: 31px; font-weight: 300; line-height: 1.3; text-transform: uppercase; margin-top: 2px; }
  .slide__button {
    display: inline-block; margin-top: 20px; width: 193px; height: 51px; line-height: 51px;
    background: var(--teal); color: var(--white); font-size: 14px; text-decoration: none;
    text-transform: uppercase; border-radius: 2px;
  }

  .pager { position: absolute; left: 1143px; top: 228px; list-style: none; }
  .pager__dot { width: 9px; height: 9px; border-radius: 50%; background: var(--dot); margin-bottom: 16px; }
  .pager__dot--active { background: transparent; border: 1px solid var(--dot); }

  .footer {
    position: absolute; left: 101px; right: 101px; top: 617px;
    display: flex; justify-content: space-between; align-items: center;
    font-size: 10px; letter-spacing: 1.4px; text-transform: uppercase;
  }
  .footer__legal span { margin: 0 12px; }
  .footer a { color: var(--white); text-decoration: none; }
  .social { display: flex; align-items: center; gap: 26px; }
  .social__label { margin-right: -8px; }
  .social__dot { width: 9px; height: 9px; border-radius: 50%; background: rgba(255,255,255,0.85); }
</style>
</head>
<body>
<main class="hero">
  <div class="hero__photo" role="img" aria-label="Photo of a young man in a blazer sitting on wooden stairs, on a phone call with a laptop on his lap"></div>
  <div class="hero__shade"></div>

  <header class="brand">
    <div class="brand__mark"></div>
    <div class="brand__name">Quillmoor</div>
  </header>

  <ul class="actions">
    <li class="actions__item">
      <svg class="actions__icon" viewBox="0 0 24 24" fill="#fff"><path d="M6.6 2.5c.6-.3 1.3-.1 1.6.5l2 3.6c.3.6.2 1.3-.3 1.7L8.4 9.5c1.2 2.6 3.3 4.8 6 6l1.2-1.5c.4-.5 1.1-.6 1.7-.3l3.6 2c.6.3.8 1 .5 1.6l-1.2 2.4c-.4.8-1.3 1.3-2.2 1.1C9.7 19.3 4.7 14.3 3.2 6.9 3 6 3.5 5.1 4.3 4.7z"/></svg>
      <div><div class="actions__title">Call me back</div><div class="actions__link">Click here &rsaquo;&rsaquo;</div></div>
    </li>
    <li class="actions__item">
      <svg class="actions__icon" viewBox="0 0 24 24" fill="none" stroke="#fff" stroke-width="2"><rect x="2.5" y="4.5" width="19" height="17" rx="1.5"/><path d="M2.5 9h19M7 2v5M17 2v5M6 12.5h3M10.5 12.5h3M15 12.5h3M6 16h3M10.5 16h3M15 16h3"/></svg>
      <div><div class="actions__title">Make an appointment</div><div class="actions__link">Click here &rsaquo;&rsaquo;</div></div>
    </li>
    <li class="actions__item">
      <svg class="actions__icon" viewBox="0 0 24 24" fill="none" stroke="#fff" stroke-width="2"><path d="M13 4H5a2 2 0 0 0-2 2v13a2 2 0 0 0 2 2h13a2 2 0 0 0 2-2v-8"/><path d="M19 2.5l2.5 2.5L12 14.5l-3.5 1 1-3.5z"/></svg>
      <div><div class="actions__title">Request a quotation</div><div class="actions__link">Click here &rsaquo;&rsaquo;</div></div>
    </li>
  </ul>

  <section class="slide">
    <h1 class="slide__title">Responsive web design</h1>
    <p class="slide__subtitle">Your website readable on all devices</p>
    <a class="slide__button" href="#">More information</a>
  </section>

  <ul class="pager">
    <li class="pager__dot pager__dot--active"></li>
    <li class="pager__dot"></li>
    <li class="pager__dot"></li>
    <li class="pager__dot"></li>
    <li class="pager__dot"></li>
  </ul>

  <footer class="footer">
    <div class="footer__legal">&copy; 2015. Quillmoor. All rights reserved.<span>/</span><a href="#">Terms &amp; Conditions</a><span>/</span><a href="#">Privacy Policy</a></div>
    <div class="social"><span class="social__label">Follow us :</span>
      <span class="social__dot"></span><span class="social__dot"></span><span class="social__dot"></span>
    </div>
  </footer>
</main>
</body>
</html>
```